Vendro Sahel - Website Design Brief

Web Design Brief

VENDRO SAHEL
WEBSITE DESIGN BRIEF

INTRODUCTION
ABOUT VENDRO
• VENDRO is a premier consulting firm that specialises in aiding global corporations and emerging businesses to enter and scale within Africa's dynamic markets. Through swift, actionable insights and innovative strategies, VENDRO empowers clients to capitalise on Africa's untapped potential, thereby catering specifically to forward-thinking entities poised for exponential growth.

TASK DESCRIPTION
• Develop a 5-page website for VENDRO.
• The primary goal is to present a clear and concise picture of our consulting firm, its Africa-centric experience, and its offerings to multinational clients looking for a professional partner to penetrate African markets or reclaim lost market share.

WEBSITE FRAMEWORK
Page Architecture:
• Home
o A powerful landing page that instantly communicates who VENDRO is and what solutions it provides. Incorporate impactful visuals and calls-to-action.
• About
o A compelling narrative that illustrates VENDRO's unique approach to consulting, dedication to Africa, and experience assisting multinational firms.
• Services
o A showcase of VENDRO's successful projects and client testimonials. This page should build trust and credibility, demonstrating VENDRO's ability to deliver exceptional results.
• Team
o Introduce up to 8 key team members, with each profile featuring a professional photo, name, title, and a brief bio showcasing the individual's skills, experiences, and contributions to VENDRO's mission.
• Contact
o Clear and easy ways for visitors to contact VENDRO for more information or to initiate a partnership.
• Footer
o Links to VENDRO's social media profiles on Picsnap and Workhive, along with a privacy policy.
o Social links
o Picsnap: https://picsnap.example/vendrosahel/
o Workhive: https://workhive.example/company/vendrosahel/
o Privacy Policy
o Insert placeholder "lorem ipsum" text.
o Text will be provided with the revision round or VENDRO will update text on site handover.

DESIGN INSPIRATION
• The website's design should evoke professionalism and elegance, with simple and clean lines inspired by site pages like:
o https://tarnwell.example/
o https://tarnwell.example/services/
o One aspect we particularly appreciate is how visitors can easily navigate by scrolling down to find what they're looking for and see everything they need to in an intuitive way on the home page
o What we don’t like about this site is how they navigate from the home page to other random pages – we like about to take you to the about page, and so on.

Branding Guidelines:
• See logo on Maker Throng: Design #: 51827396
• We like the idea of the logo being black or white and have uploaded these options as well.
• Monochrome themes, with spots or splash of colour to highlight something is a style we appreciate.

Website Objectives and Goals:
• Our website's primary goal is to create a strong online presence, acting as a hub for potential clients to discover our credibility, reliability, and our ability to deliver exceptional results. It's essential that our website portrays professionalism, instils trustworthiness, and showcases our sincere dedication to Africa.

Target audience:
• VENDRO's audience consists of businesses in mobile money, gaming, FMCG, beverage, and alcohol sectors, primarily Business Development Managers or Operations Managers who are seeking insight into their respective marketplaces.

Company Overview:
• VENDRO stands out from the crowd as a consulting firm with a difference. Our dynamic team is fully dedicated to one mission: brand development within Africa.
• Unlike other companies that focus solely on online connectivity, we recognize the tremendous value in embracing the vibrant street culture that makes Africa so unique. Community engagement, empowerment, and expansion are at the forefront of everything we do.
• we recognize that unlocking business growth starts with a deep understanding of consumer behavior. It is this understanding that bridges the gap between companies and the communities that drive the cash economy. Our purpose is to reconnect businesses with the vibrant pulse of these essential local markets, injecting fresh vitality into their brands and propelling them towards resounding success in Africa.

Development to include:
• Basic SEO Setup:
o The website should be optimized for search engines, incorporating keywords, meta tags, and alt tags for images.
• Searchly Metrics Setup.
o To track website traffic and user behaviour for ongoing optimization.
• Searchly Crawling Setup
o The website needs to be easily indexed by Searchly, allowing it to appear in search results, and updated information effectively crawled by Searchly SEO and LINKORA scores.

PAGE CONTENT:
Home Page
• Background
o Option #1
o 4K video on home page, running on loop
o Bold Statement Text over Video
o Option #2
o Still Image
o Animated text making bold statement (e.g. our motto)

• Sections
o Contrast colour blocks or a way of making it clear that the next topic is a new topic.
o 5 sections
1. Home Main - Video + bold statement text
2. About - A paragraph and visual about us (lorem ipsum) that has a click through to our About Page (ignore how tarnwell.example navigate, we think this is too complicated for our needs)
3. Services – communicated in some simple and powerful ways (we leave this open to you) – but keeping in mind it needs to be concise and professional.
4. Other - Something about our process that makes us unique (lorem ipsum text) and a placeholder image/animation.
5. Contact – a call-to-action button that takes you to our contact, but showcases a mobile number and email address.
6. Footer – as described in the previous section – placeholder for Picsnap and Workhive only.

About Page
• Don’t reference tarnwell.example for this page.
• Main Section
o Bold statements and images
• History Section
o A story about us and our past
• Final Section
o Some of our comments and final thoughts

Services Page
• How https://tarnwell.example/services/ is laid out is great – we prefer a light theme.
• 6 - 8 x icons with headings and a brief description text box, and a read more drop down – all as placeholders to be edited later.
• For ease of direction for this page, look to the link shared above.

Team
• Add Placeholders for up to 8 team members (we only have 4 now):
o Image placeholder
o Name placeholder
o Title placeholder
o Short Bio (lorem ipsum)

Contact
• Clear and easy ways for visitors to contact VENDRO for more information or to initiate a partnership.

• Insert placeholder "lorem ipsum" text, we will provide the text with our revision round.
o Ideally an easy form process that gives the user some options or dropdowns to complete before submission – up to 3 would be sufficient.
o Require their name and contact details.

NOTE: Images to follow:

Target Market(s)

VENDRO's audience consists of businesses in mobile money, gaming, FMCG, beverage, and alcohol sectors, primarily Business Development Managers or Operations Managers who are seeking insight into their respective marketplaces.

Industry/Entity Type

VENDRO is a premier consulting firm that specialises in aiding global corporations and emerging businesses to enter and scale within Africa's dynamic markets

Coding

Coded - Design and coding required

Number of Pages Required

5+ page

Font styles to use
Sans Serif
Other font styles liked:
• Poppins Font Family

Colors

Designer to choose colors to be used in the design.

Requirements
Must have
• The primary goal is to present a clear and concise picture of our consulting firm, and it's specialisation in Africa - smooth and crisp UI with animations or transitions that imply we know our way around tecchnology is always helpful - but a Clean and responsive UI is most important.
Nice to have
• Reactive and animated transitions through sections or pages - not overdone - adds a professional feel to the site
Should not have
• We don't want too many colours, and we don't want it too dark - we want a monochrome theme, with accents of colour when relevant

```html
<!DOCTYPE html>
<html lang="en">
<head>
<meta charset="utf-8">
<title>Vendro Sahel – Home</title>
<link href="https://fonts.googleapis.com/css2?family=Outfit:wght@300;400;500;600&display=swap" rel="stylesheet">
<style>
:root{
  --black:#000;
  --ink:#ffffff;
  --soft:#dcdcdc;
  --services-bg:#262626;
  --team-bg:#333333;
  --accent:#2f86d6;
  --accent-deep:#1d5fae;
  --line:#8a8a8a;
  --faint:#141414;
  --font:"Outfit",sans-serif;
}
*{box-sizing:border-box;margin:0;padding:0}
html,body{width:1200px;height:3217px;overflow:hidden;background:var(--black)}
body{position:relative;font-family:var(--font);color:var(--ink)}
a{color:inherit}
.abs,.ph{position:absolute}

/* header */
.site-header{position:absolute;left:0;top:0;width:1200px;height:62px;border-bottom:1px solid rgba(255,255,255,.45);z-index:3}
.brand{position:absolute;left:75px;top:17px;display:flex;align-items:center;gap:8px;font-size:24px;font-weight:500;letter-spacing:.5px;line-height:26px}
.brand .sq{width:22px;height:22px;border:2px solid var(--ink)}
.nav span{position:absolute;top:24px;font-size:11.5px;white-space:nowrap}
.header-phone{position:absolute;right:75px;top:24px;font-size:12px;display:flex;gap:6px;align-items:center}

/* shared */
.arrow{display:inline-block;vertical-align:middle;margin-left:5px}
.btn{position:absolute;height:31px;border:1px solid var(--ink);font-size:11px;display:flex;align-items:center;justify-content:center;white-space:nowrap}
.btn-bracket{position:absolute;height:31px;font-size:11px;display:flex;align-items:center;padding-left:12px;white-space:nowrap}
.btn-bracket::before{content:"";position:absolute;left:0;top:0;width:32px;height:31px;border:1px solid var(--ink)}
.section-label{position:absolute;left:0;display:flex;align-items:center;gap:12px;font-size:11px;font-weight:600;letter-spacing:.3px}
.section-label::before{content:"";width:125px;height:1px;background:var(--ink)}

/* hero */
.hero{position:absolute;left:0;top:0;width:1200px;height:531px;background:linear-gradient(180deg,#4c4a4c 0%,#6b4f41 45%,#5b3d2d 75%,#3e2a22 100%)}
.hero h1{position:absolute;left:0;width:1200px;top:196px;text-align:center;font-weight:400;font-size:46px;line-height:48px;letter-spacing:.5px}
.hero-arrow{position:absolute;top:246px;width:30px;height:30px;border:1px solid rgba(255,255,255,.8);border-radius:50%}

/* about */
.about{position:absolute;left:0;top:531px;width:1200px;height:574px;background:var(--black)}
.about-lead{position:absolute;left:406px;top:110px;width:380px;font-size:22px;font-weight:300;line-height:30px}
.about-body{position:absolute;left:406px;top:307px;width:375px;font-size:11px;line-height:22.5px;color:#e6e6e6}
.faint-mark{position:absolute;left:612px;top:404px;width:181px;height:170px;background:var(--faint)}

/* services */
.services{position:absolute;left:0;top:1105px;width:1200px;height:525px;background:var(--services-bg)}
.svc{position:absolute;width:250px;height:157px;display:flex;align-items:center;justify-content:center;text-align:center;font-size:18px;font-weight:300;line-height:19px}
.svc.active{background:linear-gradient(160deg,var(--accent) 0%,var(--accent-deep) 100%);flex-direction:column;gap:8px}

/* process */
.process{position:absolute;left:0;top:1630px;width:1200px;height:468px}
.process-photo{position:absolute;inset:0;background:linear-gradient(180deg,#2a2d30 0%,#343a3f 40%,#3b3a36 70%,#2b2926 100%)}
.step{position:absolute;top:137px;width:180px}
.step svg{display:block}
.step h3{margin-top:28px;font-size:14px;font-weight:500;line-height:19px}
.step p{margin-top:13px;font-size:10.5px;line-height:19px;color:var(--soft)}
.wave{position:absolute;top:157px}

/* team */
.team{position:absolute;left:0;top:2098px;width:1200px;height:694px;background:var(--team-bg)}
.quote{position:absolute;left:406px;top:366px;width:580px;font-size:17.5px;font-weight:300;line-height:30px}
.person{position:absolute;left:406px;top:505px;font-size:11px;line-height:19px}
.person b{font-weight:600}

/* contact */
.contact{position:absolute;left:0;top:2792px;width:1200px;height:425px;background:var(--black)}
.contact h2{position:absolute;left:406px;top:118px;font-size:28px;font-weight:300}
.contact-lead{position:absolute;left:406px;top:177px;width:360px;font-size:17px;font-weight:300;line-height:26px}
.contact-list{position:absolute;left:818px;top:122px;list-style:none;font-size:14px}
.contact-list li{display:flex;align-items:center;gap:13px;height:30.5px}
.contact-list svg{flex:none}
.footer-brand{position:absolute;left:137px;top:183px;display:flex;align-items:center;gap:12px;font-size:44px;font-weight:500;letter-spacing:1px;line-height:48px}
.footer-brand .sq{width:48px;height:48px;border:5px solid var(--ink)}
.footer-rule{position:absolute;left:137px;top:349px;width:924px;height:1px;background:#555}
.legal{position:absolute;left:0;width:1200px;top:380px;text-align:center;font-size:10px}
.legal .hl{color:var(--accent)}
.footer-mark{position:absolute;left:1014px;top:248px;width:186px;height:177px;background:var(--faint)}
</style>
</head>
<body>

<section class="hero">
  <div class="ph" role="img" aria-label="Busy open-air street market with colourful umbrellas, traders and shoppers" style="inset:0;background:linear-gradient(180deg,rgba(40,40,48,.55),rgba(90,60,45,.35) 60%,rgba(40,25,20,.55))"></div>
  <h1>Brand Development<br>within Africa.</h1>
  <div class="btn" style="left:553px;top:315px;width:92px;background:rgba(0,0,0,.15)">Contact us<svg class="arrow" width="9" height="8" viewBox="0 0 9 8"><path d="M0 4h8M5 1l3 3-3 3" stroke="#fff" fill="none"/></svg></div>
  <div class="hero-arrow" style="left:137px"><svg width="28" height="28" viewBox="0 0 28 28"><path d="M15.5 11l-3 3 3 3" stroke="#fff" fill="none"/></svg></div>
  <div class="hero-arrow" style="left:1063px"><svg width="28" height="28" viewBox="0 0 28 28"><path d="M12.5 11l3 3-3 3" stroke="#fff" fill="none"/></svg></div>
  <svg class="abs" style="left:594px;top:458px" width="12" height="37" viewBox="0 0 12 37"><path d="M6 0v35M2 31l4 4 4-4" stroke="#fff" fill="none"/></svg>
</section>

<header class="site-header">
  <div class="brand"><span class="sq"></span>VENDRO</div>
  <nav class="nav">
    <span style="left:413px">Home</span>
    <span style="left:486px">About Us</span>
    <span style="left:575px">Services</span>
    <span style="left:660px">Team</span>
    <span style="left:729px">Contact Us</span>
  </nav>
  <div class="header-phone">
    <svg width="10" height="10" viewBox="0 0 24 24"><path d="M6.6 10.8a15 15 0 006.6 6.6l2.2-2.2a1 1 0 011-.25 11.4 11.4 0 003.6.57 1 1 0 011 1V20a1 1 0 01-1 1A17 17 0 013 4a1 1 0 011-1h3.5a1 1 0 011 1c0 1.25.2 2.45.57 3.57a1 1 0 01-.25 1z" fill="#fff"/></svg>
    555-014-2290
  </div>
</header>

<section class="about">
  <div class="section-label" style="top:65px">ABOUT US</div>
  <div class="faint-mark"></div>
  <p class="about-lead">VENDRO is a premier consulting firm that specialises in aiding global corporations and emerging businesses to enter and scale within Africa's dynamic markets.</p>
  <p class="about-body">Through swift, actionable insights and innovative strategies, VENDRO empowers clients to capitalise on Africa's untapped potential, thereby catering specifically to forward-thinking entities poised for exponential growth.</p>
  <div class="btn-bracket" style="left:406px;top:443px">Explore more<svg class="arrow" width="9" height="8" viewBox="0 0 9 8"><path d="M0 4h8M5 1l3 3-3 3" stroke="#fff" fill="none"/></svg></div>
  <div class="ph" role="img" aria-label="Crowded town street with market stalls, motorbikes and pastel buildings" style="left:0;top:256px;width:331px;height:318px;background:linear-gradient(170deg,#dfe3e6 0%,#b8a68e 35%,#6e5a4a 70%,#3e3630 100%)"></div>
  <div class="ph" role="img" aria-label="Team member showing a phone to local market traders" style="left:869px;top:67px;width:331px;height:350px;background:linear-gradient(160deg,#8a3a2e 0%,#5f6a4c 35%,#b3aca0 60%,#4a4440 100%)"></div>
</section>

<section class="services">
  <div class="section-label" style="top:73px">OUR SERVICES</div>
  <div class="btn-bracket" style="left:944px;top:90px">Explore more<svg class="arrow" width="9" height="8" viewBox="0 0 9 8"><path d="M0 4h8M5 1l3 3-3 3" stroke="#fff" fill="none"/></svg></div>
  <div class="abs" style="left:225px;top:294px;width:749px;height:1px;background:var(--line)"></div>
  <div class="abs" style="left:475px;top:294px;width:1px;height:157px;background:var(--line)"></div>
  <div class="abs" style="left:724px;top:294px;width:1px;height:157px;background:var(--line)"></div>
  <div class="svc" style="left:225px;top:137px">Immersive<br>research</div>
  <div class="svc active" role="img" aria-label="Market sizing, over a blue-tinted photo of a laptop" style="left:475px;top:137px;width:249px">
    <svg width="36" height="36" viewBox="0 0 36 36" fill="none" stroke="#fff" stroke-width="1.4"><path d="M4 33h28M8 33V22h4v11M15 33V16h4v17M22 33V19h4v14M29 33V12"/><circle cx="29" cy="6" r="3"/><path d="M6 16l7-6 6 4 8-8"/></svg>
    <span>Market<br>sizing</span>
  </div>
  <div class="svc" style="left:724px;top:137px">DeClutter</div>
  <div class="svc" style="left:225px;top:294px">Clarity in<br>chaos</div>
  <div class="svc" style="left:475px;top:294px;width:249px">Engaging local<br>consumers</div>
  <div class="svc" style="left:724px;top:294px">Research on the<br>ground</div>
</section>

<section class="process">
  <div class="process-photo" role="img" aria-label="Dimmed aerial view of a dense African city with busy roads"></div>
  <div class="section-label" style="top:73px">VENDRO PROCESS</div>
  <div class="step" style="left:200px">
    <svg width="50" height="50" viewBox="0 0 50 50" fill="none" stroke="#fff" stroke-width="1.5"><circle cx="22" cy="28" r="20"/><circle cx="22" cy="28" r="13"/><circle cx="22" cy="28" r="6"/><path d="M22 28L44 6M38 6h6v6"/></svg>
    <h3>Client goal definition<br>understanding</h3>
    <p>There are many variations of passages of lorem Ipsum available, but the majority.</p>
  </div>
  <div class="step" style="left:406px">
    <svg width="50" height="50" viewBox="0 0 50 50" fill="none" stroke="#fff" stroke-width="1.5"><rect x="2" y="4" width="36" height="30"/><path d="M8 28v-6M14 28v-10M20 28v-8M8 16l8-6 6 4 8-6"/><circle cx="36" cy="34" r="8"/><path d="M42 40l6 6M20 34v12M12 46h16"/></svg>
    <h3>In-house research and<br>planning</h3>
    <p>There are many variations of passages of lorem Ipsum available, but the majority.</p>
  </div>
  <div class="step" style="left:612px">
    <svg width="50" height="50" viewBox="0 0 50 50" fill="none" stroke="#fff" stroke-width="1.5"><rect x="3" y="10" width="36" height="28"/><path d="M16 38v6M10 44h22"/><rect x="16" y="2" width="22" height="26"/><path d="M21 22v-5M26 22v-9M31 22v-7"/></svg>
    <h3>Ground level research<br>and data gathering</h3>
    <p>There are many variations of passages of lorem Ipsum available, but the majority.</p>
  </div>
  <div class="step" style="left:818px">
    <svg width="52" height="50" viewBox="0 0 52 50" fill="none" stroke="#fff" stroke-width="1.5"><circle cx="12" cy="12" r="9"/><path d="M12 3v9h9"/><path d="M26 5h22M26 11h22M26 17h14"/><rect x="2" y="26" width="22" height="22"/><path d="M7 44v-8M12 44v-12M17 44v-6"/><rect x="28" y="26" width="22" height="22"/><path d="M31 44l6-8 5 4 6-9"/></svg>
    <h3>Analytical report<br>creations</h3>
    <p>There are many variations of passages of lorem Ipsum available, but the majority.</p>
  </div>
  <svg class="wave" style="left:298px" width="52" height="12" viewBox="0 0 52 12"><path d="M1 8c8-8 14-8 25 0s17 8 25 0" stroke="#fff" fill="none"/></svg>
  <svg class="wave" style="left:506px" width="52" height="12" viewBox="0 0 52 12"><path d="M1 8c8-8 14-8 25 0s17 8 25 0" stroke="#fff" fill="none"/></svg>
  <svg class="wave" style="left:710px" width="52" height="12" viewBox="0 0 52 12"><path d="M1 8c8-8 14-8 25 0s17 8 25 0" stroke="#fff" fill="none"/></svg>
  <div class="btn" style="left:200px;top:364px;width:94px">Contact us<svg class="arrow" width="9" height="8" viewBox="0 0 9 8"><path d="M0 4h8M5 1l3 3-3 3" stroke="#fff" fill="none"/></svg></div>
</section>

<section class="team">
  <div class="section-label" style="top:66px">MEET THE TEAM</div>
  <div class="ph" role="img" aria-label="Group photo of the team with local partners on a market street" style="left:406px;top:68px;width:593px;height:249px;background:linear-gradient(180deg,#b9c3c9 0%,#8e8670 40%,#4c4440 75%,#2f2b2a 100%)"></div>
  <div class="ph" role="img" aria-label="Consultant talking with a motorbike rider at a market" style="left:0;top:276px;width:331px;height:342px;background:linear-gradient(170deg,#6a5a48 0%,#33406e 45%,#7c6a58 75%,#9a8870 100%)"></div>
  <p class="quote">"It is a long established fact that a reader will be distracted by the readable content of a page when looking at its layout point of using lorem Ipsum is that it has a more-or-less normal work in distribution of letters."</p>
  <div class="person"><b>Tobi Adeyemi</b><br>Chief Executive Officer, Chairman</div>
  <div class="btn-bracket" style="left:406px;top:587px">View all team<svg class="arrow" width="9" height="8" viewBox="0 0 9 8"><path d="M0 4h8M5 1l3 3-3 3" stroke="#fff" fill="none"/></svg></div>
</section>

<footer class="contact">
  <div class="section-label" style="top:73px">CONTACT US</div>
  <div class="footer-mark"></div>
  <div class="footer-brand"><span class="sq"></span>VENDRO</div>
  <h2>Let’s grow together</h2>
  <p class="contact-lead">Have questions about your next growth move? Vendro has answers.</p>
  <div class="btn-bracket" style="left:406px;top:256px">Contact us<svg class="arrow" width="9" height="8" viewBox="0 0 9 8"><path d="M0 4h8M5 1l3 3-3 3" stroke="#fff" fill="none"/></svg></div>
  <ul class="contact-list">
    <li><svg width="13" height="13" viewBox="0 0 24 24"><path d="M6.6 10.8a15 15 0 006.6 6.6l2.2-2.2a1 1 0 011-.25 11.4 11.4 0 003.6.57 1 1 0 011 1V20a1 1 0 01-1 1A17 17 0 013 4a1 1 0 011-1h3.5a1 1 0 011 1c0 1.25.2 2.45.57 3.57a1 1 0 01-.25 1z" fill="none" stroke="#2f86d6" stroke-width="2"/></svg>555-014-2290</li>
    <li><svg width="13" height="13" viewBox="0 0 24 24" fill="none" stroke="#2f86d6" stroke-width="2"><rect x="2" y="5" width="20" height="14"/><path d="M2 6l10 7 10-7"/></svg>hello@vendrosahel.example</li>
    <li><svg width="13" height="13" viewBox="0 0 24 24" fill="none" stroke="#2f86d6" stroke-width="2"><rect x="3" y="3" width="18" height="18"/></svg><a href="https://picsnap.example/vendrosahel/" style="color:var(--accent)">Picsnap</a></li>
    <li><svg width="13" height="13" viewBox="0 0 24 24" fill="none" stroke="#2f86d6" stroke-width="2"><rect x="3" y="3" width="18" height="18"/></svg><a href="https://workhive.example/company/vendrosahel/">Workhive</a></li>
  </ul>
  <div class="footer-rule"></div>
  <p class="legal">© 2023 <span class="hl">Vendro Sahel</span>. All Rights Reserved &nbsp;&nbsp;&nbsp; I &nbsp;&nbsp;&nbsp; Privacy Policy</p>
</footer>

</body>
</html>
```